Business Card

Need a clean, professional, simple, but clever business card for our company LUMO RIDES. We only want to see black and white colors as that reflects the branding of our company. Attaching logo. Will also consider the "sky blue" shown in our web site sample png - but use of the color should be minimal.

Lumo Rides is a executive car service operating in cities throughout Africa. By operating well equipped Varento Halde vehicles, we offer the smoothest and stylish ride in town. We aim to provide customers with a valuable experience. That’s why we make sure our patrons get picked up like a boss, travel in style, and arrive fabulous.

We need a card that says that. Likely to print on the best quality/smoothest paper available, as it must speak volumes of our business and class.

We would like the rear of the card to be all black. Perhaps we can put the web url on it, or leave it blank if it looks neater/more elegant.

Use the following contact information (as you see fit):

Lumo Rides Limited
P.O. Box 58104
Dar es Salaam, Tanzania

Baraka Kilonzo
Managing Director

+255 (0) 712 904618
sales@lumorides.example

web url: www.lumorides.example
email: chauffeur@lumorides.example

***Winning designer will likely be commissioned for more promotional work in near future.

Target Market(s)

The target market for this card is corporate executives of top firms (financial, consulting, businessmen, etc). They are interested in high quality transportation. Our fleet is all high end Varento Halde black cars (black exterior, black interior); and therefore, that high end quality and promptness must be reflected in the card. Also simplicity, as we we take care of all the little details behind the scene.

Industry/Entity Type

Business

Requirements
Must have
• Font must be: Helvetica Neue, like the logo. You may use other variations (Thin, Ultra thin, Regular, Bold), so long as it looks and prints well.

If web url is included on the back of the card, then do NOT include it also on the front.
Nice to have
• If there is something nice and clever that you can do/think of that doesn't make the card look busy, but adds a little "posh", then I could be even more interested.

However, if there's no little thing do be done, I'd rather a simple, but very professional looking card that attracts a lot of attention.

```html
<!DOCTYPE html>
<html lang="en">
<head>
<meta charset="utf-8">
<title>Lumo Rides — Business Card</title>
<link href="https://fonts.googleapis.com/css2?family=Arimo:wght@400;700&display=swap" rel="stylesheet">
<style>
  :root {
    --ink: #0d0d0d;
    --paper: #ffffff;
    --backdrop: #e9e9e9;
    --muted: #3a3a3a;
  }
  * { box-sizing: border-box; margin: 0; padding: 0; }
  html, body {
    width: 1200px;
    height: 871px;
    overflow: hidden;
    background: var(--backdrop);
    font-family: "Arimo", "Helvetica Neue", Helvetica, Arial, sans-serif;
  }
  .card {
    position: absolute;
    left: 280px;
    width: 640px;
    height: 366px;
    box-shadow: 0 2px 10px rgba(0,0,0,0.18);
  }
  .card--front { top: 40px; background: var(--paper); color: var(--ink); }
  .card--back  { top: 465px; background: var(--ink); color: var(--paper); }

  .brand {
    position: absolute;
    font-weight: 400;
    letter-spacing: 0.12em;
    white-space: nowrap;
  }
  .card--front .brand { top: 46px; right: 40px; font-size: 30px; }
  .card--back .brand { top: 150px; left: 0; right: 0; text-align: center; font-size: 34px; }
  .web {
    position: absolute;
    top: 198px; left: 0; right: 0;
    text-align: center;
    font-size: 12px;
    letter-spacing: 0.14em;
  }

  .name-tag {
    position: absolute;
    top: 196px; left: 0;
    width: 318px; height: 36px;
    background: var(--ink);
    color: var(--paper);
    font-weight: 700;
    font-size: 19px;
    letter-spacing: 0.08em;
    line-height: 36px;
    padding-left: 22px;
  }
  .role-row {
    position: absolute;
    top: 232px; left: 0; right: 0;
    height: 22px;
    display: flex;
  }
  .role {
    width: 300px;
    border: 1.5px solid var(--ink);
    background: var(--paper);
    font-size: 10px;
    letter-spacing: 0.12em;
    line-height: 19px;
    padding-left: 22px;
  }
  .role-band { flex: 1; background: var(--ink); }

  .contacts {
    position: absolute;
    top: 270px; left: 22px;
    font-size: 11.5px;
    line-height: 15px;
    color: var(--muted);
    display: grid;
    grid-template-columns: 48px auto;
    column-gap: 6px;
  }
  .contacts dt { font-weight: 700; color: var(--ink); text-align: right; }
  .contacts dd { letter-spacing: 0.02em; }

  .address-band {
    position: absolute;
    left: 0; right: 0; bottom: 16px;
    height: 28px;
    background: var(--ink);
    color: var(--paper);
    font-size: 11.5px;
    line-height: 28px;
    padding-left: 22px;
    letter-spacing: 0.02em;
  }
  .address-band b { font-weight: 700; }
</style>
</head>
<body>
  <section class="card card--front" aria-label="Business card front">
    <div class="brand">LUMO RIDES</div>
    <div class="name-tag">BARAKA KILONZO</div>
    <div class="role-row">
      <div class="role">MANAGING DIRECTOR</div>
      <div class="role-band"></div>
    </div>
    <dl class="contacts">
      <dt>phone:</dt><dd>+255 (0) 712 904618</dd>
      <dt>email:</dt><dd>chauffeur@lumorides.example<br>sales@lumorides.example</dd>
    </dl>
    <div class="address-band"><b>address:</b> Lumo Rides Limited, P.O. Box 58104, Dar es Salaam, Tanzania</div>
  </section>

  <section class="card card--back" aria-label="Business card back">
    <div class="brand">LUMO RIDES</div>
    <div class="web">WWW.LUMORIDES.EXAMPLE</div>
  </section>
</body>
</html>
```